Mirvane Trinkets
Lucinda Harrow Designs
Mirvane Trinkets -
Creative Brief
Simple
Lucinda Harrow
Jewelry Designer
2719 Quillfern Ln Dallas TX 75294
lucinda@mirvane-example.com
www.mirvane-example.com
Please do a few designs!
Maybe just the logo?

```html
<!DOCTYPE html>
<html lang="en">
<head>
<meta charset="utf-8">
<title>Mirvane Trinkets – Business Card</title>
<link href="https://fonts.googleapis.com/css2?family=Open+Sans:wght@400;600;700&display=swap" rel="stylesheet">
<style>
  :root {
    --backdrop: #ecdcc2;
    --card: #ffffff;
    --accent: #2fd6cf;
    --ink-strong: #555a5e;
    --ink: #6b7074;
    --mark: #9ea3a7;
  }
  html, body {
    margin: 0;
    padding: 0;
    width: 1200px;
    height: 935px;
    overflow: hidden;
    background: var(--backdrop);
    font-family: "Open Sans", Arial, sans-serif;
  }
  .canvas {
    position: relative;
    width: 1200px;
    height: 935px;
  }
  .card {
    position: absolute;
    left: 100px;
    top: 182px;
    width: 1000px;
    height: 572px;
    background: var(--card);
    border-radius: 44px;
    box-shadow: 0 6px 18px rgba(90, 70, 40, 0.18);
  }
  .edge-tab {
    position: absolute;
    width: 20px;
    height: 150px;
    background: var(--accent);
  }
  .edge-tab--left {
    left: 0;
    top: 330px;
    border-radius: 0 6px 6px 0;
  }
  .edge-tab--right {
    right: 0;
    top: 140px;
    border-radius: 6px 0 0 6px;
  }
  .brand {
    position: absolute;
    left: 110px;
    top: 215px;
    width: 270px;
    display: flex;
    flex-direction: column;
    align-items: center;
    gap: 20px;
  }
  .brand__dot {
    width: 90px;
    height: 90px;
    border-radius: 50%;
    background: var(--mark);
  }
  .brand__name {
    font-size: 30px;
    font-weight: 400;
    color: var(--ink);
    letter-spacing: 1px;
    white-space: nowrap;
  }
  .contact {
    position: absolute;
    right: 105px;
    top: 120px;
    width: 470px;
    text-align: right;
    color: var(--ink);
  }
  .contact__name {
    margin: 0;
    font-size: 30px;
    font-weight: 700;
    color: var(--ink-strong);
  }
  .contact__role {
    margin: 4px 0 0;
    font-size: 20px;
    font-weight: 600;
    color: var(--ink-strong);
  }
  .contact__details {
    margin: 70px 0 0;
    font-size: 21px;
    line-height: 1.5;
  }
  .contact__details span { display: block; white-space: nowrap; }
  .contact__label { font-weight: 700; }
</style>
</head>
<body>
<main class="canvas">
  <section class="card" aria-label="Mirvane Trinkets business card">
    <div class="edge-tab edge-tab--left"></div>
    <div class="edge-tab edge-tab--right"></div>

    <div class="brand">
      <div class="brand__dot"></div>
      <div class="brand__name">Mirvane Trinkets</div>
    </div>

    <div class="contact">
      <h1 class="contact__name">Lucinda Harrow</h1>
      <p class="contact__role">Jewelry Designer</p>
      <p class="contact__details">
        <span>2719 Quillfern Ln Dallas TX 75294</span>
        <span><b class="contact__label">Phone :</b> 214-555-0187</span>
        <span><b class="contact__label">Email :</b> lucinda@mirvane-example.com</span>
        <span><b class="contact__label">Web :</b> www.mirvane-example.com</span>
      </p>
    </div>
  </section>
</main>
</body>
</html>
```